Need a Chatterly design page for our site velvet harbor crew

the website is velvetharborcrew (dot) com

The site is about helping people get into modelling. they sign up on the site we give them a call if we think they have potential to become a model. We are looking for a design for our Chatterly page we want the design to be as stunning as the website is.

Target Market(s)

People who want to become models

Industry/Entity Type

Call

Font styles to use
Sans Serif

Requirements
Must have
• Must look like the website
Nice to have
• Would like to it to look and have the same theme as the chatterly

```html
<!DOCTYPE html>
<html lang="en">
<head>
<meta charset="utf-8">
<title>Velvet harbor crew – Chatterly cover</title>
<link href="https://fonts.googleapis.com/css2?family=Roboto+Condensed:wght@700&display=swap" rel="stylesheet">
<style>
  :root {
    --tone-light: #c8ab92;
    --tone-mid: #a88670;
    --tone-skin: #c39682;
    --tone-dark: #5b4137;
    --tone-deep: #3f2c25;
    --headline: #141010;
    --headline-glow: rgba(255, 240, 225, 0.85);
    --button-fill: rgba(70, 50, 42, 0.55);
    --button-edge: rgba(235, 215, 200, 0.55);
    --button-text: #ffffff;
  }
  html, body {
    margin: 0;
    padding: 0;
    overflow: hidden;
    background: #ffffff;
  }
  .cover {
    position: relative;
    width: 1200px;
    height: 628px;
    overflow: hidden;
    font-family: "Roboto Condensed", "Arial Narrow", sans-serif;
  }
  .cover__backdrop {
    position: absolute;
    inset: 0;
    background:
      radial-gradient(ellipse 260px 200px at 900px 330px, var(--tone-skin) 0%, transparent 100%),
      radial-gradient(ellipse 300px 240px at 780px 80px, var(--tone-dark) 0%, transparent 100%),
      radial-gradient(ellipse 220px 420px at 1150px 300px, var(--tone-deep) 0%, transparent 100%),
      radial-gradient(ellipse 380px 160px at 200px 470px, #e2d2c4 0%, transparent 100%),
      linear-gradient(100deg, var(--tone-light) 0%, var(--tone-mid) 45%, #8a6656 75%, var(--tone-dark) 100%);
  }
  .cover__headline {
    position: absolute;
    top: 110px;
    left: 0;
    width: 100%;
    margin: 0;
    text-align: center;
    font-size: 53px;
    font-weight: 700;
    line-height: 82px;
    letter-spacing: 0.5px;
    color: var(--headline);
    text-shadow: 0 0 8px var(--headline-glow), 0 0 16px var(--headline-glow);
  }
  .cover__cta {
    position: absolute;
    left: 428px;
    top: 392px;
    width: 380px;
    height: 82px;
    box-sizing: border-box;
    display: flex;
    align-items: center;
    justify-content: center;
    background: var(--button-fill);
    border: 2px solid var(--button-edge);
    color: var(--button-text);
    font-size: 29px;
    font-weight: 700;
    letter-spacing: 0.5px;
    text-transform: uppercase;
  }
</style>
</head>
<body>
  <main class="cover">
    <div class="cover__backdrop" role="img" aria-label="Soft-focus photograph of a young woman resting her chin on her hand in warm beige tones"></div>
    <h1 class="cover__headline">Velvet harbor crew helps aspiring<br>models break into the modelling world</h1>
    <div class="cover__cta">Register yourself</div>
  </main>
</body>
</html>
```